Nest Sack new product

Re-usable baby food pouch. Need artwork for new product.
Primarily green, some clear space (1/3 - 1/2 clear) so you can see through to whats inside.

To be fresh, organic looking and to appeal to kids and families.

Portrait style 18xm long, 11cm wide.

Need a front and back version (both this size)

please see similar products on www.brightmorsels.example and www.tinyfernsack.example

Target Market(s)

Families, kids product

Industry/Entity Type

Baby

Colors
9ccb3b

Requirements
Must have
• Clear space as described.
Under Logo
"reusable food pouch"
BPA Free- dishwasher safe- freezer safe

On back
Logo
Tick boxes
Freezer safe
dishwasher safe
BPA Phthalate & PVC Free
160 mls
DO NOT MICROWAVE

"to warm contents simply place filled pouch in a bowl of hot water" Keep the cap out of reach of children 3 and under.

www.nestsacks.example.au

```html
<!DOCTYPE html>
<html lang="en">
<head>
<meta charset="utf-8">
<title>Nest Sack – reusable food pouch, front and back</title>
<link rel="stylesheet" href="https://fonts.googleapis.com/css2?family=Open+Sans:wght@400;600;700&display=swap">
<style>
  :root {
    --backdrop: #e4e4e4;
    --pouch-green: #95b51c;
    --seal-green: #86a414;
    --ink-white: #ffffff;
    --contents-light: #c98a1e;
    --contents-dark: #a86a12;
  }
  * { margin: 0; padding: 0; box-sizing: border-box; }
  html, body { width: 1200px; height: 675px; overflow: hidden; }
  body {
    background: var(--backdrop);
    font-family: "Open Sans", Arial, sans-serif;
    color: var(--ink-white);
    position: relative;
  }
  .pouch {
    position: absolute;
    top: 35px;
    width: 352px;
    height: 610px;
    background: var(--pouch-green);
    border-radius: 6px 6px 4px 4px;
    overflow: hidden;
  }
  .pouch--front { left: 162px; }
  .pouch--back { left: 686px; }
  .pouch__seal {
    position: absolute; left: 0; top: 0; width: 100%; height: 40px;
    background: var(--seal-green);
  }
  .brand {
    position: absolute; left: 0; width: 100%;
    display: flex; align-items: center; justify-content: center;
    font-weight: 700; line-height: 1; white-space: nowrap;
  }
  .brand__dot { border-radius: 50%; background: var(--ink-white); flex: none; }
  .pouch--front .brand { top: 118px; height: 56px; font-size: 46px; gap: 12px; }
  .pouch--front .brand__dot { width: 52px; height: 52px; }
  .pouch--back .brand { top: 64px; height: 40px; font-size: 32px; gap: 10px; }
  .pouch--back .brand__dot { width: 36px; height: 36px; }
  .tagline {
    position: absolute; left: 0; width: 100%; text-align: center; font-weight: 600;
    white-space: nowrap;
  }
  .pouch--front .tagline { top: 188px; font-size: 27px; line-height: 34px; }
  .pouch--back .tagline { top: 120px; font-size: 17px; line-height: 22px; font-weight: 400; }
  .front-claims {
    position: absolute; top: 255px; left: 0; width: 100%;
    text-align: center; font-size: 22px; font-weight: 600; line-height: 33px;
  }
  .window {
    position: absolute; left: 18px; top: 390px; width: 316px; height: 220px;
    border-radius: 158px 158px 0 0 / 60px 60px 0 0;
    background: linear-gradient(180deg, var(--contents-light), var(--contents-dark));
  }
  .info-box {
    position: absolute; left: 34px; top: 162px; width: 284px; height: 340px;
    border: 2px solid var(--ink-white); border-radius: 14px;
  }
  .checklist { position: absolute; left: 26px; top: 20px; list-style: none; }
  .checklist li {
    display: flex; align-items: center; gap: 10px;
    font-size: 24px; font-weight: 600; line-height: 37px; white-space: nowrap;
  }
  .checklist li.continued { padding-left: 34px; }
  .checklist svg { width: 24px; height: 24px; flex: none; }
  .instructions {
    position: absolute; left: 12px; top: 176px; width: 262px;
    font-size: 13px; line-height: 16px; font-weight: 600;
  }
  .instructions p + p { margin-top: 16px; }
  .volume {
    position: absolute; left: 0; top: 275px; width: 100%;
    text-align: center; font-size: 24px; font-weight: 700;
  }
  .warning {
    position: absolute; left: 0; top: 313px; width: 100%;
    text-align: center; font-size: 16px; font-weight: 600;
  }
  .web {
    position: absolute; left: 0; top: 507px; width: 100%;
    text-align: center; font-size: 20px; font-weight: 700; white-space: nowrap;
  }
</style>
</head>
<body>
  <section class="pouch pouch--front" aria-label="Front of pouch">
    <div class="pouch__seal"></div>
    <div class="brand"><span class="brand__dot"></span><span>Nest Sack</span></div>
    <p class="tagline">reusable food pouch</p>
    <div class="front-claims">
      <p>BPA Free</p>
      <p>dishwasher safe</p>
      <p>freezer safe</p>
    </div>
    <div class="window" role="img" aria-label="Clear window showing the food inside the pouch"></div>
  </section>

  <section class="pouch pouch--back" aria-label="Back of pouch">
    <div class="pouch__seal"></div>
    <div class="brand"><span class="brand__dot"></span><span>Nest Sack</span></div>
    <p class="tagline">reusable food pouch</p>
    <div class="info-box">
      <ul class="checklist">
        <li><svg viewBox="0 0 24 24" aria-hidden="true"><rect x="2" y="4" width="18" height="18" fill="none" stroke="#fff" stroke-width="2"/><path d="M6 12 L11 17 L22 2" fill="none" stroke="#fff" stroke-width="2.5"/></svg>Freezer safe</li>
        <li><svg viewBox="0 0 24 24" aria-hidden="true"><rect x="2" y="4" width="18" height="18" fill="none" stroke="#fff" stroke-width="2"/><path d="M6 12 L11 17 L22 2" fill="none" stroke="#fff" stroke-width="2.5"/></svg>Dishwasher safe</li>
        <li><svg viewBox="0 0 24 24" aria-hidden="true"><rect x="2" y="4" width="18" height="18" fill="none" stroke="#fff" stroke-width="2"/><path d="M6 12 L11 17 L22 2" fill="none" stroke="#fff" stroke-width="2.5"/></svg>BPA Phthalate</li>
        <li class="continued">&amp; PVC Free</li>
      </ul>
      <div class="instructions">
        <p>To warm contents simply place filled<br>pouch in a bowl of hot water.</p>
        <p>Keep the cap out of reach of<br>children 3 and under.</p>
      </div>
      <p class="volume">160 mls</p>
      <p class="warning">DO NOT MICROWAVE</p>
    </div>
    <p class="web">www.nestsacks.example.au</p>
  </section>
</body>
</html>
```